Photographic Tutorial website

We are looking for a fresh design for a photographic tutorial / workshop website. The website will have the included functions:

* Home (needs to have a login section)
* About Us
* Info about each course / workshop.
* Subscribe to courses and pay online.
* Members Area
* Photo gallery
* Contact us

The website will be implemented with our own made cms. We do not need it to be coded. We have a team ready to do this for us. We only need the PSD layout.

We have attached a mockup design that the client and I have come up with and we need the design to be taken to the next level.

Client also likes:
http://www.vellowindstudio.example/

Photographic Interests

Online

Requirements
Must have
• Must Stand out i.e black backgrounds
Should not have
• Alter the logo in anyway.

```html
<!DOCTYPE html>
<html lang="en">
<head>
<meta charset="utf-8">
<title>Lens Mate Studio – Photographic Tuition</title>
<link href="https://fonts.googleapis.com/css2?family=Arimo:wght@400;700&display=swap" rel="stylesheet">
<style>
:root{
  --page:#121212;
  --band:#1c1c1c;
  --red:#a3131b;
  --red-dark:#6e0b10;
  --red-text:#e0282f;
  --nav:#4a3f38;
  --nav-line:#5d524a;
  --text:#e6e6e6;
  --muted:#7a7a7a;
  --white:#ffffff;
}
*{box-sizing:border-box;margin:0;padding:0}
html,body{width:1200px;height:971px;overflow:hidden;background:var(--page);font-family:"Arimo",Arial,sans-serif;color:var(--text)}
.canvas{position:relative;width:1200px;height:971px;background:repeating-linear-gradient(45deg,#141414 0 2px,#101010 2px 4px)}
.top-bar{position:absolute;left:0;top:0;width:1200px;height:49px;background:linear-gradient(#2a2a2a,#141414)}
.brand{position:absolute;left:225px;top:0;width:304px;height:65px;background:#1a1a1a;border:1px solid #333;display:flex;align-items:center;gap:10px;padding-left:14px;z-index:3}
.brand-dot{width:26px;height:26px;border-radius:50%;background:var(--red)}
.brand-name{font-size:27px;font-weight:700;color:var(--white)}
.account{position:absolute;left:860px;top:17px;display:flex;gap:16px;font-size:10px;color:var(--white)}
.account span{display:flex;align-items:center;gap:5px}
.hero{position:absolute;left:0;top:49px;width:1200px;height:289px;background:linear-gradient(180deg,#c9c3b9 0%,#e7cfa8 25%,#dcb989 60%,#c89f6c 100%);border-bottom:3px solid #555}
.main-nav{position:absolute;left:226px;top:88px;width:304px;z-index:2}
.main-nav a{display:flex;justify-content:space-between;align-items:center;height:37.6px;padding:0 12px 0 13px;background:rgba(60,50,44,.88);border-bottom:1px solid var(--nav-line);color:var(--white);font-size:14px;text-decoration:none}
.main-nav a.active{background:rgba(163,19,27,.92)}
.icon{width:16px;height:16px;border-radius:3px}
.carousel{position:absolute;left:230px;top:357px;width:739px;height:134px;background:var(--white)}
.slide{position:absolute;top:10px;width:112px}
.slide-photo{height:86px}
.slide-label{height:27px;background:var(--red);color:var(--white);font-size:11px;display:flex;align-items:center;justify-content:center}
.arrow{position:absolute;top:43px;width:22px;height:36px;background:var(--white)}
.arrow.prev{left:0;border-radius:0 18px 18px 0}
.arrow.next{right:0;border-radius:18px 0 0 18px}
.col-title{position:absolute;font-size:13px;color:var(--white)}
.photo{position:absolute}
.caption{position:absolute;background:var(--red);color:var(--white);font-size:9px;line-height:13px;padding:5px 7px}
.caption .author{position:absolute;right:10px;bottom:6px;color:#1a1a1a}
.link-box{position:absolute;left:233px;top:762px;width:198px;height:122px;background:linear-gradient(90deg,var(--red),var(--red-dark));padding:9px 0 0 12px}
.link-box li{list-style:none;font-size:10px;font-weight:700;color:#f5c9c9;height:23px;padding-left:7px;position:relative}
.link-box li::before{content:"";position:absolute;left:0;top:3px;border:3px solid transparent;border-left:4px solid #3a0407}
.blog-post{position:absolute;left:459px;width:286px;border-bottom:1px solid #3a3a3a;padding-bottom:7px}
.blog-head{display:flex;justify-content:space-between;font-size:10px;padding:0 30px 0 2px;margin-bottom:5px}
.blog-head .title{color:var(--red-text)}
.blog-head .date{color:var(--white);font-size:9px}
.blog-post p{font-size:9px;line-height:13px;color:var(--muted)}
.check-box{position:absolute;left:764px;top:765px;width:197px;height:71px;background:linear-gradient(90deg,var(--red),var(--red-dark));padding:7px 0 0 10px}
.check-box li{list-style:none;display:flex;align-items:center;gap:10px;height:19.5px;font-size:9px;font-weight:700;color:#2a0306}
.footer{position:absolute;left:0;top:906px;width:1200px;height:65px;background:var(--band);border-top:1px solid #2c2c2c}
.footer-brand{position:absolute;left:233px;top:22px;display:flex;align-items:center;gap:10px;font-size:8px;color:var(--muted)}
.footer-brand .brand-dot{width:18px;height:18px}
.follow{position:absolute;left:753px;top:14px;width:194px;height:37px;background:#1e1e1e;border:1px solid #3a3a3a;display:flex;align-items:center;justify-content:space-between;padding:0 14px;font-size:14px;font-weight:700;letter-spacing:1px;color:#9a9a9a}
</style>
</head>
<body>
<div class="canvas">
  <header class="top-bar">
    <div class="account">
      <span><svg width="11" height="11" viewBox="0 0 11 11"><path d="M4 1H1v9h3M4 5.5h6M7 3l3 2.5L7 8" stroke="#4fb6e8" fill="none" stroke-width="1.5"/></svg>Sign In</span>
      <span><svg width="11" height="11" viewBox="0 0 11 11"><circle cx="4" cy="4" r="3" stroke="#4fb6e8" fill="none" stroke-width="1.5"/><path d="M6 6l4 4" stroke="#4fb6e8" stroke-width="1.8"/></svg>Sign Up</span>
    </div>
  </header>
  <div class="brand"><span class="brand-dot"></span><span class="brand-name">Lens Mate Studio</span></div>

  <div class="hero" role="img" aria-label="Photographer lying on desert sand dunes taking a picture with a camera"></div>

  <nav class="main-nav">
    <a class="active" href="#">HOME <svg class="icon" viewBox="0 0 16 16"><path d="M2 8L8 2l6 6v7H2z" fill="#f3e6d0"/><rect x="6.5" y="10" width="3" height="5" fill="#c0392b"/></svg></a>
    <a href="#">ABOUT US <svg class="icon" viewBox="0 0 16 16"><circle cx="8" cy="8" r="8" fill="#2e6fd6"/><rect x="7" y="7" width="2" height="6" fill="#fff"/><circle cx="8" cy="4.5" r="1.2" fill="#fff"/></svg></a>
    <a href="#">COURSE/WORKSHOP INFO <svg class="icon" viewBox="0 0 16 16"><rect x="3" y="1" width="10" height="14" rx="1" fill="#2a8fb8"/><rect x="4.5" y="3" width="7" height="9" fill="#bfe8f6"/></svg></a>
    <a href="#">MEMBERS AREA <svg class="icon" viewBox="0 0 16 16"><circle cx="5" cy="6" r="3" fill="#d8a878"/><circle cx="11" cy="6" r="3" fill="#caa070"/><rect x="1" y="10" width="14" height="6" rx="3" fill="#3b7bb0"/></svg></a>
    <a href="#">PHOTO GALLERY <svg class="icon" viewBox="0 0 16 16"><rect x="1" y="2" width="14" height="12" fill="#e8e8e8"/><rect x="2.5" y="3.5" width="11" height="9" fill="#7cc1e8"/><path d="M2.5 12.5l4-4 3 3 2-2 2 3z" fill="#5b9b3e"/></svg></a>
    <a href="#">CONTACT US <svg class="icon" viewBox="0 0 16 16"><path d="M2 6c0-3 12-3 12 0v2h-3V6H5v2H2z" fill="#3aa0d8"/><rect x="3" y="8" width="10" height="6" rx="1" fill="#3aa0d8"/></svg></a>
  </nav>

  <section class="carousel">
    <div class="slide" style="left:10px"><div class="slide-photo" role="img" aria-label="Old stone alley" style="background:linear-gradient(#b9b3a8,#8c8478)"></div><div class="slide-label">Urber Photography</div></div>
    <div class="slide" style="left:131px"><div class="slide-photo" role="img" aria-label="Tree and goats on dry ground" style="background:linear-gradient(#6b5a48,#b3a08a)"></div><div class="slide-label">Urber Photography</div></div>
    <div class="slide" style="left:252px"><div class="slide-photo" role="img" aria-label="Country road under blue sky" style="background:linear-gradient(#7fa8d8,#d6c288 60%,#8a7a58)"></div><div class="slide-label">Urber Photography</div></div>
    <div class="slide" style="left:373px"><div class="slide-photo" role="img" aria-label="Black and white antelope" style="background:linear-gradient(#9a9a9a,#3a3a3a)"></div><div class="slide-label">Urber Photography</div></div>
    <div class="slide" style="left:494px"><div class="slide-photo" role="img" aria-label="Person holding a camera" style="background:linear-gradient(#5a4a42,#c8b0a0)"></div><div class="slide-label">Urber Photography</div></div>
    <div class="slide" style="left:615px"><div class="slide-photo" role="img" aria-label="White horses by the water" style="background:linear-gradient(#4f7a3a,#2f5f8a)"></div><div class="slide-label">Urber Photography</div></div>
    <span class="arrow prev"></span><span class="arrow next"></span>
  </section>

  <h2 class="col-title" style="left:233px;top:506px">Testimonial</h2>
  <div class="photo" role="img" aria-label="Rolled certificate tied with a red ribbon" style="left:231px;top:533px;width:198px;height:154px;background:linear-gradient(135deg,#f0f0f0,#b8b8b8)"></div>
  <div class="caption" style="left:231px;top:687px;width:198px;height:38px">Lorem Ipsum is simply dummy text of the and typesetting industry.<span class="author">Dana Reyes</span></div>

  <h2 class="col-title" style="left:233px;top:736px">Links</h2>
  <ul class="link-box">
    <li>General Information</li>
    <li>Daily Shooting Times</li>
    <li>Nautical Twilight statt to end</li>
    <li>Moon face chart</li>
    <li>Link &amp; Review</li>
  </ul>

  <h2 class="col-title" style="left:459px;top:506px">Blog</h2>
  <article class="blog-post" style="top:532px"><div class="blog-head"><span class="title">Us Photography in 2012</span><span class="date">21st june,2012</span></div><p>Lorem Ipsum is simply dummy text of the printing and typesetting indus-try. Lorem Ipsum has been the industry's standard dummy text ever</p></article>
  <article class="blog-post" style="top:596px"><div class="blog-head"><span class="title">Us Photography in 2012</span><span class="date">21st june,2012</span></div><p>Lorem Ipsum is simply dummy text of the printing and typesetting indus-try. Lorem Ipsum has been the industry's standard dummy text ever</p></article>
  <article class="blog-post" style="top:663px"><div class="blog-head"><span class="title">Us Photography in 2012</span><span class="date">21st june,2012</span></div><p>Lorem Ipsum is simply dummy text of the printing and typesetting indus-try. Lorem Ipsum has been the industry's standard dummy text ever</p></article>
  <article class="blog-post" style="top:731px"><div class="blog-head"><span class="title">Us Photography in 2012</span><span class="date">21st june,2012</span></div><p>Lorem Ipsum is simply dummy text of the printing and typesetting indus-try. Lorem Ipsum has been the industry's standard dummy text ever</p></article>
  <article class="blog-post" style="top:798px;border-bottom:none"><div class="blog-head"><span class="title">Us Photography in 2012</span><span class="date">21st june,2012</span></div><p>Lorem Ipsum is simply dummy text of the printing and typesetting indus-try. Lorem Ipsum has been the industry's standard dummy text ever</p></article>

  <h2 class="col-title" style="left:770px;top:507px">Members Gallery</h2>
  <div class="photo" role="img" aria-label="Grid of member photos showing a white goat on sand" style="left:768px;top:533px;width:198px;height:155px;background:linear-gradient(#3a2f28,#9a8470 50%,#5a4a3e)"></div>
  <div class="caption" style="left:768px;top:688px;width:198px;height:42px">Lorem Ipsum is simply dummy text of the print-ing and typesetting m Ipsum is simply dummy</div>

  <h2 class="col-title" style="left:771px;top:742px">Photographers Check List</h2>
  <ul class="check-box">
    <li><svg width="14" height="12" viewBox="0 0 14 12"><path d="M1 6l4 4 8-9" stroke="#fff" stroke-width="2.4" fill="none"/></svg>Wedding Check Lists</li>
    <li><svg width="14" height="12" viewBox="0 0 14 12"><path d="M1 6l4 4 8-9" stroke="#fff" stroke-width="2.4" fill="none"/></svg>Pre shoot Check Lists</li>
    <li><svg width="14" height="12" viewBox="0 0 14 12"><path d="M1 6l4 4 8-9" stroke="#fff" stroke-width="2.4" fill="none"/></svg>Standard Check Lists</li>
  </ul>

  <footer class="footer">
    <div class="footer-brand"><span class="brand-dot"></span>All Rights Reserved to Lens Mate Studio</div>
    <div class="follow">FOLLOW US ON <svg width="22" height="24" viewBox="0 0 22 24"><path d="M4 23L8 2" stroke="#bbb" stroke-width="1.5"/><path d="M8 2c5 3 8-2 13 1l-3 10c-5-3-8 2-13-1z" fill="#2a6fd0"/></svg></div>
  </footer>
</div>
</body>
</html>
```